Tall Harbor Business Card

We are a Video Production and Video Equipment Rental company specialising in the supply of state of the art Video Technology and Services for the Live Entertainment, Television and Corporate Business Theatre markets. (in Sydney, Australia) www.tallharbor-media.example

Industry/Entity Type

Business

Contact Information for Business Card

name, position, email, website, address, logo
Example attached of the information we need - doesn't necessarily have to look the same

Font styles to use
Other font styles liked:
• Tall Harbor logo font is GOTHAM

Colors
ea1f27

Requirements
Nice to have
• either matt black or shiny black cards -
raised logo

```html
<!DOCTYPE html>
<html lang="en">
<head>
<meta charset="utf-8">
<title>Tall Harbor – Business Card</title>
<link rel="stylesheet" href="https://fonts.googleapis.com/css2?family=Montserrat:wght@500;600&family=Open+Sans:wght@400;600&display=swap">
<style>
  :root {
    --harbor-red: #ea1f27;
    --ink-black: #0d0d0d;
    --paper-white: #f4f3f1;
    --stage-grey: #e4e4e4;
    --text-dark: #1c1c1c;
    --text-light: #ffffff;
  }
  * { box-sizing: border-box; margin: 0; padding: 0; }
  html, body {
    width: 1200px; height: 777px; overflow: hidden;
    background: var(--stage-grey);
    font-family: "Open Sans", Arial, sans-serif;
  }
  .canvas { position: relative; width: 1200px; height: 777px; }

  .card {
    position: absolute; width: 520px; height: 300px; overflow: hidden;
    box-shadow: 0 6px 18px rgba(0,0,0,0.18);
  }
  .card--front { left: 60px; top: 130px; background: var(--paper-white); color: var(--text-dark); }
  .card--back  { left: 620px; top: 347px; background: var(--harbor-red); color: var(--text-light); }

  .brand {
    position: absolute; display: flex; align-items: center; gap: 14px;
    font-family: "Montserrat", Arial, sans-serif; font-weight: 500;
    font-size: 34px; line-height: 1; letter-spacing: 1px; text-transform: uppercase;
  }
  .brand__square { width: 12px; height: 12px; background: var(--harbor-red); }
  .card--front .brand { left: 40px; top: 46px; color: var(--text-dark); }

  .logo-band {
    position: absolute; left: 0; top: 28px; width: 100%; height: 80px;
    background: var(--ink-black);
  }
  .card--back .brand { left: 40px; top: 23px; color: var(--text-light); }

  .contact {
    position: absolute; right: 36px; width: 340px; text-align: right;
  }
  .card--front .contact { top: 104px; }
  .card--back .contact { top: 120px; }

  .contact__name {
    text-align: left; font-weight: 600; font-size: 25px; line-height: 1.2; letter-spacing: -0.3px;
    padding-bottom: 3px; border-bottom: 2px solid currentColor;
  }
  .contact__role { font-size: 15px; line-height: 1.3; margin-top: 3px; }
  .contact__address { font-size: 13px; line-height: 1.35; font-weight: 600; margin-top: 6px; }
  .contact__web { font-size: 13px; line-height: 1.35; font-weight: 600; margin-top: 8px; }

  .services {
    position: absolute; left: 0; bottom: 0; width: 100%; height: 40px;
    display: flex; align-items: center; justify-content: space-between;
    padding: 0 18px; font-size: 12.5px; line-height: 1; text-transform: uppercase; letter-spacing: 0.3px;
    color: var(--text-light);
  }
  .card--front .services { background: var(--harbor-red); }
  .card--back .services { background: var(--ink-black); }
  .services__divider { color: var(--text-light); }
</style>
</head>
<body>
<main class="canvas">

  <section class="card card--front" aria-label="Business card, white side">
    <div class="brand"><span class="brand__square"></span><span>Tall Harbor</span></div>
    <div class="contact">
      <p class="contact__name">Marco Vellani</p>
      <p class="contact__role">Managing Director</p>
      <p class="contact__address">12 Quay Lane, Pyrmont, NSW 2009, Australia</p>
      <p class="contact__web">marco@tallharbor-media.example<br>www.tallharbor-media.example</p>
    </div>
    <div class="services">
      <span>Video Solutions</span><span class="services__divider">|</span>
      <span>LED Screens</span><span class="services__divider">|</span>
      <span>Camera Systems</span><span class="services__divider">|</span>
      <span>Projection</span>
    </div>
  </section>

  <section class="card card--back" aria-label="Business card, red side">
    <div class="logo-band">
      <div class="brand"><span class="brand__square"></span><span>Tall Harbor</span></div>
    </div>
    <div class="contact">
      <p class="contact__name">Marco Vellani</p>
      <p class="contact__role">Managing Director</p>
      <p class="contact__address">12 Quay Lane, Pyrmont, NSW 2009, Australia</p>
      <p class="contact__web">marco@tallharbor-media.example<br>www.tallharbor-media.example</p>
    </div>
    <div class="services">
      <span>Video Solutions</span><span class="services__divider">|</span>
      <span>LED Screens</span><span class="services__divider">|</span>
      <span>Camera Systems</span><span class="services__divider">|</span>
      <span>Projection</span>
    </div>
  </section>

</main>
</body>
</html>
```